Orthopedic Landing Page Website Design

We are working with a Orthopedic Medical Group in California. They provide orthopedic services throughout California.

Some sites to use for inspiration:
https://www.trelvakhealth.com
https://brisenclinic.com
https://www.kolvendaboneclinic.com
https://halbertonjointcare.com

Thank you for taking the time to consider designing a website for us. We are web developers based in Stockton, CA, USA. Most of our projects go through the same process. Understanding this process may help you win a project with us. We custom-code all of our websites in-house. We don’t have any requirements as to what tools you use for your design, but we ask that you follow these guidelines.

IMAGES:
If you use any images or icons in the design, we ask that you have a link to the asset so we can purchase the image/icon. Most of the designs we submit do not have the customer’s images on them unless they have some great images. Be creative; show us the feeling you are trying to portray with your image choices. Use any royalty-free site you choose. We subscribe to Verlio and mainly use their images, but we can purchase images outside of Verlio. PLEASE NOTE: we will not submit designs to clients with watermarks on the images.

FONTS:
We ask that you identify the fonts you’re using in the design. This can be done in a message if you want. We typically use Pamquist Fonts and Verlio Fonts.

CONTENT:
We're always open to different content and ideas. We often submit designs with stock images so the client can see our vision. We typically take pictures after the website launch to use their images with our vision. Lorem Ipsum is fine for paragraphs, but we ask that you make the Headers with correct English. We want to be able to show the vision and identify the sections of the website.

INSPIRATION:
We typically add a couple of links in the brief of websites we like to help you get started in your design.

REVISIONS:
We do not often ask for revisions of the designs unless we see something in the design that may not appeal to the client. If there are slight changes that we want to make, we do that in the development process.

FEEDBACK:
We rarely give feedback on designs during the design process. We are working on many website projects and do not have the time to provide feedback. We usually respond if your request is well thought out and asks specific questions, but a note asking “feedback, please” usually goes unanswered.

```html
<!DOCTYPE html>
<html lang="en">
<head>
<meta charset="utf-8">
<title>Norvale Orthopedic</title>
<link href="https://fonts.googleapis.com/css2?family=PT+Serif:wght@400;700&family=PT+Sans:wght@400;700&display=swap" rel="stylesheet">
<style>
:root{
  --blue:#1f6399;
  --blue-dark:#184f7c;
  --red:#c8203a;
  --ink:#2b2b2b;
  --pale:#eef5fb;
  --white:#ffffff;
  --serif:'PT Serif', Georgia, serif;
  --sans:'PT Sans', Arial, sans-serif;
}
*{box-sizing:border-box;margin:0;padding:0}
html,body{width:1200px;height:4079px;overflow:hidden}
body{position:relative;background:var(--white);font-family:var(--sans);color:var(--ink)}
.abs{position:absolute}
.img-fill{position:absolute}

/* header */
.brand{position:absolute;display:flex;align-items:center;gap:10px;font-family:var(--serif);font-weight:400;color:var(--blue);letter-spacing:2px;white-space:nowrap}
.brand .dot{width:34px;height:34px;border-radius:50%;border:2px solid var(--blue);flex:none}
.header .brand{left:103px;top:30px;font-size:24px}
.search{position:absolute;left:664px;top:32px;width:268px;height:40px;border:1.5px solid var(--blue);border-radius:20px;font-family:var(--serif);font-size:14px;color:var(--blue);padding:10px 12px}
.search .btn{position:absolute;right:3px;top:3px;width:32px;height:32px;border-radius:50%;background:var(--blue)}
.pill{position:absolute;display:flex;align-items:center;justify-content:center;border-radius:22px;font-family:var(--serif);font-weight:700;font-size:14px;color:var(--white);background:var(--red)}
.nav{position:absolute;left:0;top:99px;width:1200px;height:51px;background:var(--blue);display:flex;justify-content:center;gap:45px;align-items:center;font-family:var(--serif);font-size:14px;color:var(--white)}

/* hero */
.hero{position:absolute;left:0;top:150px;width:1200px;height:650px;background:linear-gradient(90deg,#5e5e5e,#9a9a9a 70%,#bdbdbd)}
.hero h1{position:absolute;left:104px;top:112px;font-family:var(--serif);font-weight:400;font-size:40px;line-height:46px;color:var(--white)}
.hero p{position:absolute;left:104px;top:216px;width:480px;font-size:14px;line-height:23px;color:var(--white)}
.hero .outline{position:absolute;left:104px;top:326px;width:237px;height:42px;border:2px solid var(--white);border-radius:22px;color:var(--white);font-family:var(--serif);font-weight:700;font-size:13px;display:flex;align-items:center;justify-content:center}

/* section heads */
.mark{position:absolute;width:34px;height:34px;border-radius:50%;border:2px solid var(--blue)}
.title{position:absolute;font-family:var(--serif);font-weight:400;font-size:29px;color:var(--blue);text-transform:uppercase;white-space:nowrap}
.rule{position:absolute;width:40px;height:3px;background:var(--red)}
.lead{position:absolute;left:104px;width:992px;text-align:center;font-size:16px;line-height:26px}

/* about */
.about{position:absolute;left:0;top:790px;width:1200px;height:740px;background:linear-gradient(120deg,#ffffff 30%,#e6f3fa)}
.about .name{position:absolute;left:631px;top:247px;font-family:var(--serif);font-size:28px;color:var(--red)}
.about .copy{position:absolute;left:631px;top:295px;width:400px;font-size:15px;line-height:24px}
.about .copy p{margin-bottom:8px}

/* services */
.services{position:absolute;left:0;top:1530px;width:1200px;height:907px;background:var(--blue)}
.services .title,.services .lead{color:var(--white)}
.card{position:absolute;width:233px;height:248px;overflow:hidden}
.card .shade{position:absolute;inset:0;background:linear-gradient(180deg,rgba(0,0,0,0) 55%,rgba(0,0,0,.65))}
.card span{position:absolute;left:0;right:0;bottom:24px;text-align:center;font-family:var(--serif);font-weight:700;font-size:17px;color:var(--white)}

/* reviews */
.reviews{position:absolute;left:0;top:2437px;width:1200px;height:595px;background:var(--pale)}
.reviews p{position:absolute;left:103px;top:190px;width:440px;font-size:15px;line-height:26px}
.stars{position:absolute;left:103px;top:362px;color:#f2b01e;font-size:16px;letter-spacing:1px}
.reviewer{position:absolute;left:103px;top:390px;font-family:var(--serif);font-size:19px;color:var(--red)}
.arrow{position:absolute;top:432px;width:36px;height:36px;border-radius:50%;display:flex;align-items:center;justify-content:center}

/* contact */
.contact{position:absolute;left:0;top:3032px;width:1200px;height:703px;background:linear-gradient(110deg,#ffffff 10%,#d7ecf8 55%,#4fb9ec)}
.form-card{position:absolute;left:104px;top:85px;width:496px;height:588px;background:var(--white);border-radius:14px;box-shadow:0 4px 18px rgba(0,0,0,.15)}
.field{position:absolute;left:33px;width:413px;height:50px;background:#eaf1f8;border:1.5px solid var(--blue);font-family:var(--serif);font-weight:700;font-size:15px;color:var(--blue);padding:14px 14px}

/* footer */
.footer{position:absolute;left:0;top:3735px;width:1200px;height:344px;background:var(--white)}
.footer h4{position:absolute;top:28px;font-family:var(--serif);font-weight:400;font-size:22px;color:var(--blue)}
.links{position:absolute;left:375px;top:68px;font-family:var(--serif);font-size:14px;line-height:25.5px}
.info{position:absolute;left:574px;display:flex;align-items:center;gap:16px;font-family:var(--serif);font-size:14px;line-height:21px}
.info .ic{width:38px;height:38px;border-radius:50%;background:var(--red);display:flex;align-items:center;justify-content:center;flex:none}
.social{position:absolute;top:135px;width:34px;height:34px;border-radius:50%;background:var(--blue)}
.copyright{position:absolute;left:0;top:297px;width:1200px;text-align:center;font-size:13px}
</style>
</head>
<body>

<header class="header">
  <div class="brand"><span class="dot"></span>NORVALE ORTHOPEDIC</div>
  <div class="search">Search<span class="btn">
    <svg width="32" height="32" viewBox="0 0 32 32"><circle cx="15" cy="15" r="5" fill="none" stroke="#fff" stroke-width="2"/><line x1="18.5" y1="18.5" x2="22" y2="22" stroke="#fff" stroke-width="2"/></svg></span></div>
  <div class="pill" style="left:945px;top:32px;width:150px;height:40px">APPOINTMENTS</div>
</header>

<nav class="nav">
  <span>About</span><span>Areas Of Specialty</span><span>Our Doctors</span><span>Patient Resources</span><span>Research</span><span>Blog</span><span>Contact Us</span><span>Locations</span>
</nav>

<section class="hero">
  <div class="img-fill" role="img" aria-label="Photo: patient with back and neck pain, spine highlighted" style="left:660px;top:0;width:540px;height:650px;background:linear-gradient(90deg,rgba(150,150,150,0),#8a8480 40%,#a49f9b)"></div>
  <h1>WELCOME TO NORVALE<br>ORTHOPEDIC GROUP</h1>
  <p>Lorem ipsum dolor sit amet, consectetur adipiscing elit, sed do eiusmod tempor incididunt ut labore et dolore magna aliqua. Quis ipsum suspendisse ultrices gravida. Risus commodo viverra maecenas accumsan lacus vel facilisis.</p>
  <div class="outline">BOOK AN APPOINTMENTS</div>
  <svg class="abs" style="left:0;top:440px" width="1200" height="220" viewBox="0 0 1200 220" preserveAspectRatio="none">
    <path d="M0 120 C200 40 420 90 620 150 C820 210 1020 210 1200 70 L1200 220 L0 220Z" fill="var(--blue)"/>
    <path d="M0 130 C200 50 420 100 620 160 C820 220 1020 225 1200 95 L1200 220 L0 220Z" fill="#f4fafd"/>
  </svg>
</section>

<section class="about">
  <span class="mark" style="left:583px;top:43px"></span>
  <h2 class="title" style="left:0;width:1200px;text-align:center;top:85px">About Norvale Orthopedic</h2>
  <span class="rule" style="left:580px;top:127px"></span>
  <p class="lead" style="top:146px">Lorem ipsum dolor sit amet, consectetur adipiscing elit, sed do eiusmod tempor incididunt ut labore et dolore magna aliqua. Quis ipsum suspendisse ultrices gravida. Risus commodo viverra maecenas accumsan lacus vel facilisis.</p>
  <div class="img-fill" role="img" aria-label="Smiling doctor in a white coat holding a tablet in his office" style="left:170px;top:237px;width:383px;height:421px;border-radius:30px;background:linear-gradient(160deg,#cfd6dc,#9aa7b2 50%,#5e6c78)"></div>
  <div class="name">M. Deloran, MD, FAAOS</div>
  <div class="copy">
    <p>Lorem ipsum dolor sit amet, consectetur adipiscing elit, sed do eiusmod tempor incididunt ut labore et dolore magna aliqua. Quis ipsum suspendisse ultrices gravida. Risus commodo viverra maecenas accumsan lacus vel facilisis.</p>
    <p>Sed ut perspiciatis unde omnis iste natus error sit voluptatem accusantium doloremque laudantium, totam rem aperiam, eaque ipsa quae ab illo inventore veritatis et quasi architecto beatae vitae dicta sunt explicabo. Nemo enim ipsam voluptatem quia voluptas sit aspernatur aut odit aut fugit, sed quia consequuntur magni dolores eos qui ratione .</p>
  </div>
  <div class="pill" style="left:631px;top:600px;width:158px;height:40px;font-size:13px">MEET OUR TEAM</div>
</section>

<section class="services">
  <span class="mark" style="left:583px;top:52px;border-color:#fff"></span>
  <h2 class="title" style="left:0;width:1200px;text-align:center;top:92px">Our Services</h2>
  <span class="rule" style="left:580px;top:135px;background:#fff"></span>
  <p class="lead" style="top:154px">Lorem ipsum dolor sit amet, consectetur adipiscing elit, sed do eiusmod tempor incididunt ut labore et dolore magna aliqua. Quis ipsum suspendisse ultrices gravida. Risus commodo viverra maecenas accumsan lacus vel facilisis.</p>

  <div class="card" style="left:104px;top:238px" role="img" aria-label="Older woman holding her knee on a sofa"><div class="img-fill" style="inset:0;background:linear-gradient(160deg,#e4e2dc,#b7b2a6)"></div><div class="shade"></div><span>Joint Replacement</span></div>
  <div class="card" style="left:357px;top:238px" role="img" aria-label="Woman holding her painful wrist"><div class="img-fill" style="inset:0;background:linear-gradient(160deg,#d8d6d0,#7d7a74)"></div><div class="shade"></div><span>Hand &amp; Wrist</span></div>
  <div class="card" style="left:610px;top:238px" role="img" aria-label="Doctor pointing at a foot bone model"><div class="img-fill" style="inset:0;background:linear-gradient(160deg,#e9eef3,#b5c3d0)"></div><div class="shade"></div><span>Foot &amp; Ankle</span></div>
  <div class="card" style="left:862px;top:238px" role="img" aria-label="Older man holding his back"><div class="img-fill" style="inset:0;background:linear-gradient(160deg,#c9c9c9,#6e6e6e)"></div><div class="shade"></div><span>Spine</span></div>
  <div class="card" style="left:104px;top:505px" role="img" aria-label="Trainer helping a man lift dumbbells"><div class="img-fill" style="inset:0;background:linear-gradient(160deg,#dfe3e6,#7b8794)"></div><div class="shade"></div><span>Sports Medicine</span></div>
  <div class="card" style="left:357px;top:505px" role="img" aria-label="Woman with lower back pain sitting on a bed"><div class="img-fill" style="inset:0;background:linear-gradient(160deg,#f2f2f2,#b9b9b9)"></div><div class="shade"></div><span>Intervention Pain</span></div>
  <div class="card" style="left:610px;top:505px" role="img" aria-label="Hands holding a painful knee"><div class="img-fill" style="inset:0;background:linear-gradient(160deg,#7a4434,#3a2520)"></div><div class="shade"></div><span>Knee</span></div>
  <div class="card" style="left:862px;top:505px" role="img" aria-label="Woman running outdoors"><div class="img-fill" style="inset:0;background:linear-gradient(160deg,#dde6ec,#a9b7c0)"></div><div class="shade"></div><span>Hip</span></div>
</section>

<section class="reviews">
  <span class="mark" style="left:103px;top:130px"></span>
  <h2 class="title" style="left:151px;top:128px">Patient Reviews</h2>
  <span class="rule" style="left:151px;top:170px"></span>
  <p>Lorem ipsum dolor sit amet, consectetur adipiscing elit, sed do eiusmod tempor incididunt ut labore et dolore magna aliqua. Ut enim ad minim veniam, quis nostrud exercitation ullamco laboris nisi ut aliquip ex ea commodo consequat. Duis aute irure dolor in reprehenderit in voluptate velit esse cillum dolore eu fugiat nulla pariatur.</p>
  <div class="stars">★★★★★</div>
  <div class="reviewer">Marisol</div>
  <div class="arrow" style="left:103px;background:var(--red)"><svg width="16" height="16" viewBox="0 0 16 16"><path d="M13 8H3M7 4L3 8l4 4" stroke="#fff" stroke-width="2" fill="none"/></svg></div>
  <div class="arrow" style="left:148px;background:#fff;box-shadow:0 1px 4px rgba(0,0,0,.2)"><svg width="16" height="16" viewBox="0 0 16 16"><path d="M3 8h10M9 4l4 4-4 4" stroke="var(--blue)" stroke-width="2" fill="none"/></svg></div>
  <svg class="abs" style="left:670px;top:110px" width="410" height="410" viewBox="0 0 410 410">
    <path d="M95 370 A190 190 0 0 1 300 40" stroke="var(--blue)" stroke-width="10" fill="none"/>
    <path d="M345 80 A190 190 0 0 1 130 388" stroke="var(--red)" stroke-width="6" fill="none"/>
  </svg>
  <div class="img-fill" role="img" aria-label="Physiotherapist examining a young woman's knee in a clinic" style="left:697px;top:137px;width:356px;height:356px;border-radius:50%;background:linear-gradient(150deg,#e9eef2,#b3bdc6 60%,#7c8792)"></div>
</section>

<section class="contact">
  <div class="img-fill" role="img" aria-label="Smiling female doctor with stethoscope pointing to the side" style="left:640px;top:40px;width:430px;height:663px;background:linear-gradient(180deg,rgba(240,240,240,.9),rgba(255,255,255,.95))"></div>
  <svg class="abs" style="left:0;top:560px" width="1200" height="143" viewBox="0 0 1200 143" preserveAspectRatio="none"><path d="M0 60 C250 120 500 80 750 40 C950 10 1100 40 1200 70 L1200 143 L0 143Z" fill="#fff"/></svg>
  <div class="form-card">
    <span class="mark" style="left:33px;top:45px"></span>
    <h2 class="title" style="left:80px;top:43px">Contact Us Today</h2>
    <span class="rule" style="left:80px;top:85px"></span>
    <div class="field" style="top:113px">Name</div>
    <div class="field" style="top:178px">phone Number</div>
    <div class="field" style="top:243px">Email</div>
    <div class="field" style="top:308px;height:155px">Message</div>
    <div class="pill" style="left:33px;top:481px;width:133px;height:42px">SUBMIT</div>
  </div>
</section>

<footer class="footer">
  <div class="brand" style="left:103px;top:40px;font-size:16px;letter-spacing:1px"><span class="dot"></span>NORVALE ORTHOPEDIC</div>
  <span class="social" style="left:103px"></span><span class="social" style="left:150px"></span><span class="social" style="left:197px"></span>
  <h4 style="left:375px">Quick LInks</h4>
  <div class="links">About<br>Areas Of Specialty<br>Our Doctors<br>Patient Resources<br>Research<br>Blog<br>Contact Us<br>Locations</div>
  <h4 style="left:574px">Contact Us</h4>
  <div class="info" style="top:70px"><span class="ic"><svg width="18" height="18" viewBox="0 0 18 18"><path d="M9 1a6 6 0 0 0-6 6c0 4.5 6 10 6 10s6-5.5 6-10a6 6 0 0 0-6-6z" fill="#fff"/><circle cx="9" cy="7" r="2.2" fill="var(--red)"/></svg></span><span>2840 Ridgeway Ave, Suite C<br>Fairmont, CA 95310</span></div>
  <div class="info" style="top:135px"><span class="ic"><svg width="18" height="18" viewBox="0 0 18 18"><path d="M4 2l3 3-2 2c1 2 3 4 5 5l2-2 3 3-2 3C8 16 2 10 2 4z" fill="#fff"/></svg></span><span>+1 555 014 2290</span></div>
  <div class="info" style="top:186px"><span class="ic"><svg width="18" height="18" viewBox="0 0 18 18"><rect x="2" y="4" width="14" height="10" fill="#fff"/><path d="M2 4l7 6 7-6" stroke="var(--red)" stroke-width="1.5" fill="none"/></svg></span><span>info@norvaleortho.com</span></div>
  <h4 style="left:865px">Newsletter</h4>
  <div class="search" style="left:865px;top:66px;width:271px;height:40px;font-size:15px">Enter Email</div>
  <div class="pill" style="left:1002px;top:124px;width:133px;height:40px">SUBMIT</div>
  <div class="copyright">© 2023 Norvale Orthopedic &nbsp;| All Rights Reserved</div>
</footer>

</body>
</html>
```